Business Card Design - Photographer

I am a landscape photographer and I require a business card design. 

I require two designs:
1)  a double sided business card
 and
b)  a single sided business card 

The single sided design can either be the same as the double sided (with just one side having all the information)....or it can be an entire new design. Its up to you.

My corporate colours are (CMYK):

Blue   69, 32, 0, 0
Grey  72,  64,  47,  31
Green  32,  2,  91,  0
Yellow   0, 19, 92, 0
Orange  0, 39, 75, 0

Colour space in final file should be in CMYK.

The details that need to be included on the card:

- Use the provided Logo
- Name: Lukas Wendrovski
- Email:   sales@vistaplume.com.au
- Website:    vistaplume.com.au
- Twitter:    twitter.com/vistaplume
- Facebook:   facebook.com/vistaplume
- Mobile  0415 309 662

Please use the attached template to design the logo to the specified size, including the marked bleed lines. I have also attached my logo in PNG (transparent background) and ai format for you to use.

The final file should be:
- Photoshop version with layers so I can edit the name/text etc. All non vector files should be high resolution at 1039 x 697 pixels at 300 dpi.

I also require a file as:
- Vector based PDF

Anyway questions please contact me.

Thank you

Industry/Entity Type

Landscape

Logo styles of interest
Pictorial/Combination Logo
Abstract Logo
Wordmark Logo
Lettermark Logo
Requirements
Must have
• The details that need to be included on the card:

- Use the provided Logo
- Name: Lukas Wendrovski
- Email: sales@vistaplume.com.au
- Website: vistaplume.com.au
- Twitter: twitter.com/vistaplume
- Facebook: facebook.com/vistaplume
- Mobile 0415 309 662

```html
<!DOCTYPE html>
<html lang="en">
<head>
<meta charset="utf-8">
<title>Vista Plume — Business Cards</title>
<link rel="stylesheet" href="https://fonts.googleapis.com/css2?family=Cinzel:wght@400;500;600&display=swap">
<style>
  :root {
    --backdrop: #7f8084;
    --card: #ffffff;
    --ink: #3a3f50;
    --brand-blue: #3d8fce;
    --brand-green: #a9cc3a;
    --shadow: rgba(0, 0, 0, 0.35);
  }
  * { margin: 0; padding: 0; box-sizing: border-box; }
  html, body {
    width: 978px;
    height: 1200px;
    overflow: hidden;
    background: var(--backdrop);
  }
  .canvas {
    position: relative;
    width: 978px;
    height: 1200px;
  }
  .card {
    position: absolute;
    left: 93px;
    width: 788px;
    height: 453px;
    background: var(--card);
    border-radius: 28px;
    overflow: hidden;
    transform: scale(1.038);
    transform-origin: top left;
    box-shadow: 4px 6px 10px var(--shadow);
    font-family: "Cinzel", "Times New Roman", serif;
    color: var(--ink);
  }
  .card--front { top: 95px; }
  .card--back { top: 647px; }

  .card__waves {
    position: absolute;
    inset: 0;
    width: 788px;
    height: 453px;
  }

  .brand-mark {
    position: absolute;
    left: 64px;
    top: 42px;
    width: 168px;
    height: 168px;
    border-radius: 50%;
    background: var(--ink);
  }
  .brand-name {
    position: absolute;
    left: 268px;
    top: 86px;
    width: 456px;
    font-size: 43px;
    font-weight: 500;
    letter-spacing: 1px;
    line-height: 1;
    text-align: center;
    color: var(--ink);
    white-space: nowrap;
  }
  .brand-rule {
    position: absolute;
    left: 268px;
    top: 139px;
    width: 456px;
    height: 2px;
    background: var(--ink);
  }
  .brand-tagline {
    position: absolute;
    left: 268px;
    top: 150px;
    width: 456px;
    text-align: center;
    font-size: 17px;
    font-weight: 600;
    letter-spacing: 3px;
    white-space: nowrap;
  }

  .website {
    position: absolute;
    right: 40px;
    top: 360px;
    font-size: 14px;
    font-weight: 600;
    letter-spacing: 0.5px;
    white-space: nowrap;
  }
  .website__domain { font-size: 21px; }

  .contact {
    position: absolute;
    left: 380px;
    top: 306px;
    width: 400px;
    list-style: none;
    text-align: center;
    font-size: 16px;
    line-height: 32px;
    letter-spacing: 0.3px;
    white-space: nowrap;
  }
</style>
</head>
<body>
<main class="canvas">

  <section class="card card--front" aria-label="Business card front">
    <svg class="card__waves" viewBox="0 0 788 453" aria-hidden="true">
      <path fill="var(--brand-green)" d="M0,285 C150,302 280,300 420,255 C560,212 700,206 788,206 L788,222 C700,223 560,234 440,270 C300,312 150,324 0,306 Z"/>
      <path fill="var(--brand-blue)" d="M0,325 C150,346 300,340 430,292 C560,246 690,240 788,262 L788,453 L0,453 Z"/>
      <path fill="none" stroke="#ffffff" stroke-width="2" d="M40,367 C200,386 330,362 470,308 C600,264 720,256 788,262"/>
    </svg>
    <div class="brand-mark" aria-hidden="true"></div>
    <h1 class="brand-name">VISTA PLUME</h1>
    <div class="brand-rule"></div>
    <p class="brand-tagline">FINE ART PHOTOGRAPHY</p>
    <p class="website">www.<span class="website__domain">VISTAPLUME</span>.com.au</p>
  </section>

  <section class="card card--back" aria-label="Business card back">
    <svg class="card__waves" viewBox="0 0 788 453" aria-hidden="true">
      <path fill="var(--brand-green)" d="M0,285 C150,302 280,300 420,255 C560,212 700,206 788,206 L788,222 C700,223 560,234 440,270 C300,312 150,324 0,306 Z"/>
      <path fill="var(--brand-blue)" d="M0,325 C150,346 300,340 430,292 C560,246 690,240 788,262 L788,453 L0,453 Z"/>
      <path fill="none" stroke="#ffffff" stroke-width="2" d="M40,367 C200,386 330,362 470,308 C600,264 720,256 788,262"/>
    </svg>
    <div class="brand-mark" aria-hidden="true"></div>
    <h2 class="brand-name">VISTA PLUME</h2>
    <div class="brand-rule"></div>
    <p class="brand-tagline">FINE ART PHOTOGRAPHY</p>
    <ul class="contact">
      <li>E : sales@vistaplume.com.au</li>
      <li>T : twitter.com/vistaplume</li>
      <li>F : facebook.com/vistaplume</li>
      <li>M : 0415 309 662</li>
    </ul>
  </section>

</main>
</body>
</html>
```